Redesign of page from emergency manual

Please redesign this PDF to look better. Please don't include any stock photos. It must be legible. Making some words bold is probably a good idea.

Here are some things I like :

https://brambolthouse.com.au/collections/frontpage/products/the-kvt-v2-ebook

https://media-qz.fennowstatic.net/kd-pqRwTbnVYy_ZaWsLmHu400K4sa-Xe9vbPqTn37sJdVRwaT4PiedfxrmZ8NTcUjK=w1052-h592-rw

```html
<!DOCTYPE html>
<html lang="en">
<head>
<meta charset="utf-8">
<title>Hypertension, Acute</title>
<link rel="stylesheet" href="https://fonts.googleapis.com/css2?family=Noto+Sans:ital,wght@0,400;0,600;0,700;0,800;1,700&display=swap">
<style>
:root{
  --band:#6ee8fc;
  --band-deep:#16b9d4;
  --cell-head:#b9f5fd;
  --row-tint:#eefcfe;
  --ink:#0b1a1e;
  --soft-ink:#33474c;
  --line:#1d2c30;
  --caution-bg:#fff6e5;
  --caution-edge:#f0a020;
  --muted:#6d8a90;
  --paper:#fff;
}
*{box-sizing:border-box;margin:0;padding:0}
html,body{width:1200px;height:927px;overflow:hidden;background:var(--paper)}
body{font-family:"Noto Sans",Verdana,sans-serif;color:var(--ink);position:relative}

.top-band{position:absolute;left:0;top:0;width:1143px;height:60px;background:var(--band)}
.side-band{position:absolute;left:1143px;top:0;width:57px;height:927px;background:var(--band)}
.page-title{position:absolute;left:40px;top:5px;font-size:37px;font-weight:800;letter-spacing:.3px;line-height:50px}
.definition{position:absolute;left:660px;top:5px;width:462px;height:50px;background:var(--paper);border:2px solid var(--line);border-radius:10px;
  font-size:15.5px;font-weight:700;font-style:italic;text-align:center;line-height:20px;padding-top:4px}
.page-number{position:absolute;left:1143px;top:66px;width:57px;text-align:center;font-size:26px;font-weight:800;color:var(--ink)}
.side-title{position:absolute;left:1192px;top:250px;transform-origin:0 0;transform:rotate(90deg);white-space:nowrap;font-size:36px;font-weight:800}
.revision{position:absolute;left:1180px;top:765px;transform-origin:0 0;transform:rotate(90deg);white-space:nowrap;font-size:13px;color:var(--muted)}

/* intro */
.intro{position:absolute;left:40px;top:76px;width:605px;font-size:18px;line-height:25px}
.intro .lead{position:relative;padding-left:20px}
.intro .lead::before{content:"";position:absolute;left:0;top:9px;width:8px;height:8px;background:var(--band-deep)}
.intro ul{list-style:none;margin:10px 0 0 24px}
.intro li{position:relative;padding-left:20px;margin-bottom:9px}
.intro li::before{content:"•";position:absolute;left:2px;color:var(--band-deep);font-weight:800}
.intro li.sub{margin-left:40px;color:var(--soft-ink)}
.intro li.sub::before{content:"–";color:var(--soft-ink)}

/* bp range */
.bp-card{position:absolute;left:680px;top:78px;width:432px;border:2px solid var(--line);border-radius:10px;overflow:hidden}
.bp-table{width:100%;border-collapse:collapse;font-size:17px;text-align:center}
.bp-table th,.bp-table td{border-bottom:1.5px solid var(--line);height:34px}
.bp-table th + th,.bp-table td + td{border-left:1.5px solid var(--line)}
.bp-table tr:last-child td{border-bottom:none}
.bp-table .caption-row th{background:var(--cell-head);height:38px;font-weight:800}
.bp-table .col-row th{font-weight:700;background:var(--row-tint)}
.bp-table td.age{font-weight:600}

/* caution */
.caution{position:absolute;left:40px;top:290px;width:1072px;background:var(--caution-bg);border-left:6px solid var(--caution-edge);border-radius:6px;
  padding:8px 14px 8px 16px;font-size:17px;line-height:24px}
.caution b{font-weight:800}

/* drug table */
.drug-card{position:absolute;left:40px;top:385px;width:1072px;border:2px solid var(--line);border-radius:10px;overflow:hidden}
.drug-table{width:100%;border-collapse:collapse;font-size:19px;line-height:25px}
.drug-table th,.drug-table td{vertical-align:top;border-bottom:1.5px solid var(--line)}
.drug-table tr:last-child td{border-bottom:none}
.drug-table th + th,.drug-table td + td{border-left:1.5px solid var(--line)}
.drug-table th{background:var(--cell-head);height:44px;font-size:22px;font-weight:800;vertical-align:middle;text-align:center}
.drug-table tr:nth-child(odd) td{background:var(--row-tint)}
.drug-table .action{width:310px;font-weight:800;padding:10px 14px}
.drug-table ul{list-style:none;padding:9px 12px 7px 14px}
.drug-table li{position:relative;padding-left:24px;margin-bottom:4px}
.drug-table li::before{content:"";position:absolute;left:0;top:9px;width:8px;height:8px;background:var(--band-deep)}
.drug-table .name{font-weight:700}

/* differential */
.diff-head{position:absolute;left:40px;top:725px;font-size:20px;line-height:26px;padding-left:20px}
.diff-head::before{content:"";position:absolute;left:0;top:9px;width:8px;height:8px;background:var(--band-deep)}
.diff-head b{font-weight:800}
.diff-col{position:absolute;list-style:none;font-size:18.5px;line-height:23px}
.diff-col li{position:relative;padding-left:20px;margin-bottom:8px}
.diff-col li::before{content:"•";position:absolute;left:2px;color:var(--band-deep);font-weight:800}
.diff-col b{font-weight:800}
.c1{left:64px;top:762px;width:330px}
.c2{left:430px;top:762px;width:380px}
.c3{left:860px;top:762px;width:260px}
</style>
</head>
<body>
<div class="top-band"></div>
<div class="side-band"></div>
<h1 class="page-title">Hypertension, Acute</h1>
<div class="definition">Sustained high blood pressure refractory<br>to treating reversible causes</div>
<div class="page-number">12</div>
<div class="side-title">Hypertension, Acute</div>
<div class="revision">Revision Feb 2020</div>

<section class="intro">
  <p class="lead">In pediatrics, hypertension is almost always treated by addressing likely causes such as <b>light anesthesia</b> or <b>measurement error</b>:</p>
  <ul>
    <li>Ensure correct <b>BP cuff size</b>: cuff bladder width ~ 40% of limb circumference</li>
    <li>Ensure <b>arterial line transducer</b> is at level of heart</li>
    <li class="sub">Consider placing arterial line if not already present</li>
  </ul>
</section>

<div class="bp-card">
<table class="bp-table">
  <tr class="caption-row"><th colspan="3">Hypertensive Blood Pressure Range*</th></tr>
  <tr class="col-row"><th>Age (yr)</th><th>Systolic</th><th>Diastolic</th></tr>
  <tr><td class="age">Newborn</td><td>&gt;97</td><td>&gt;70</td></tr>
  <tr><td class="age">1-3</td><td>&gt;105</td><td>&gt;61</td></tr>
  <tr><td class="age">4-12</td><td>&gt;113</td><td>&gt;86</td></tr>
</table>
</div>

<p class="caution">* <b>CAUTION:</b> Anti-hypertensive drugs are <b>almost never needed</b> for routine pediatric cases. These medications are used almost exclusively for specialized cardiac, neurosurgical, or endocrine (pheochromocytoma) cases. <b>Consult an expert before use. Rule-out increased ICP.</b></p>

<div class="drug-card">
<table class="drug-table">
  <tr><th>Action</th><th>Drug (IV Dosing)</th></tr>
  <tr><td class="action">Direct smooth muscle relaxation</td><td><ul>
    <li><span class="name">Sodium nitroprusside</span> 0.5-10 MICROgrams/kg/min</li>
    <li><span class="name">HydrALAZINE</span> 0.1-0.2 mg/kg (adult dose 5-10 mg)</li></ul></td></tr>
  <tr><td class="action">β-Adrenergic blockade</td><td><ul>
    <li><span class="name">Esmolol</span> 100-500 MICROgrams/kg over 5 min, then 25-300 MICROgrams/kg/min</li>
    <li><span class="name">Labetalol</span> (also α effect) 0.2-1 mg/kg q 10 min; 0.4-3 mg/kg/<i>hour</i> (infusion)</li></ul></td></tr>
  <tr><td class="action">Calcium channel blockade</td><td><ul>
    <li><span class="name">niCARdapine</span> 0.5-5 MICROgrams/kg/min</li>
    <li><span class="name">Clevidipine</span> 0.5-3.5 MICROgrams/kg/min</li></ul></td></tr>
  <tr><td class="action">D1-dopamine agonist</td><td><ul>
    <li><span class="name">Fenoldopam</span> 0.2-0.8 MICROgrams/kg/min</li></ul></td></tr>
</table>
</div>

<div class="diff-head"><b>Consider Differential</b> (Partial):</div>
<ul class="diff-col c1">
  <li><b>Light anesthesia</b> (consider vaporizer or infusion pump empty or malfunctioning)</li>
  <li><b>Hypercarbia</b></li>
</ul>
<ul class="diff-col c2">
  <li><b>Hypoxemia</b></li>
  <li><b>Arterial line transducer</b> too low or BP cuff too small</li>
  <li><b>Withdrawal</b> (EtOH or opioid)</li>
</ul>
<ul class="diff-col c3">
  <li><b>Thyroid Storm</b></li>
  <li><b>Pheochromocytoma</b></li>
  <li><b>Drug Error</b></li>
</ul>
</body>
</html>
```